Need Help having my business card stand out

I am the owner of Pine Ridge Canine Coaching and would like for my business cards to stand out. I have been trying to keep designing them myself but I can't get what I have in my head on the card. I will try my best to post templates that I like for inspirations. I want something unique but elegant. I don't want in to look cartoony or cheesy. It needs to pop in a pet shop but also in a coffee shop or gym.

Target Market(s)

Dog owners, Married ,No young kids Jr High school kids and up (maybe kids on the way) Executives, Stay at home moms/wives, Small business owners

Industry/Entity Type

Dog Training

Contact Information for Business Card

Trevor Holloway, 555-304-7162, info@pineridgecanine.example, www.pineridgecanine.example

Colors

Designer to choose colors to be used in the design.

Requirements
Must have
• my logo
Should not have
• Cursive lettering

```html
<!DOCTYPE html>
<html lang="en">
<head>
<meta charset="utf-8">
<title>Pine Ridge Canine Coaching – Business Cards</title>
<link href="https://fonts.googleapis.com/css2?family=Lato:wght@700;900&display=swap" rel="stylesheet">
<style>
  :root {
    --bronze: #7a5522;
    --bronze-dark: #6a4a1c;
    --ink: #1b1b1b;
    --paper: #efeeec;
    --page: #ffffff;
    --sepia-light: #c9ad84;
    --sepia-mid: #a8885a;
    --sepia-deep: #7d6038;
  }
  * { box-sizing: border-box; margin: 0; padding: 0; }
  html, body { width: 1200px; height: 1200px; overflow: hidden; background: var(--page); }
  body { position: relative; font-family: 'Lato', sans-serif; }

  .card {
    position: absolute;
    top: 181px;
    width: 478px;
    height: 840px;
    background: var(--paper);
    overflow: hidden;
  }
  .card--rounded { left: 122px; border-radius: 130px 0 130px 0; }
  .card--angled { left: 646px; width: 480px; }

  .card__photo {
    position: absolute;
    left: 0; top: 0;
    width: 100%; height: 391px;
    background: linear-gradient(160deg, var(--sepia-deep) 0%, var(--sepia-mid) 40%, var(--sepia-light) 75%, var(--sepia-mid) 100%);
  }

  .card__brand {
    position: absolute;
    left: 32px; top: 262px;
    display: flex; align-items: center; gap: 10px;
    width: 230px;
  }
  .card__brand-dot {
    flex: 0 0 auto;
    width: 34px; height: 34px;
    border-radius: 50%;
    background: var(--ink);
  }
  .card__brand-name {
    font-weight: 900;
    font-size: 21px;
    line-height: 1.1;
    color: var(--ink);
    text-transform: uppercase;
  }

  .card__name {
    position: absolute;
    left: 40px; top: 430px;
    font-weight: 900;
    font-size: 34px;
    letter-spacing: 0.2px;
    color: var(--ink);
    white-space: nowrap;
  }
  .card__name-first { color: var(--bronze); }
  .card__role {
    position: absolute;
    left: 40px; top: 481px;
    font-weight: 700;
    font-size: 20px;
    letter-spacing: 2.6px;
    color: var(--ink);
  }

  .card__divider {
    position: absolute;
    left: 92px; top: 560px;
    width: 3px; height: 188px;
    background: var(--bronze);
  }
  .contact {
    position: absolute;
    left: 0; width: 100%;
    height: 30px;
    display: flex; align-items: center;
  }
  .contact__icon {
    position: absolute;
    left: 40px;
    width: 30px; height: 30px;
    stroke: var(--bronze);
    fill: none;
    stroke-width: 1.6;
  }
  .contact__text {
    position: absolute;
    left: 130px;
    font-weight: 700;
    font-size: 14.5px;
    letter-spacing: 1.3px;
    color: var(--ink);
    white-space: nowrap;
  }
  .contact--phone { top: 577px; }
  .contact--email { top: 638px; }
  .contact--web { top: 697px; }

  .card__accent { position: absolute; fill: var(--bronze-dark); }
  .card__accent--top { left: 0; top: 0; }
  .card__accent--bottom { right: 0; bottom: 0; }
</style>
</head>
<body>

  <!-- Rounded variant -->
  <section class="card card--rounded">
    <div class="card__photo" role="img" aria-label="Sepia photo of a trainer standing with three seated dogs on a leafy lawn"></div>
    <div class="card__brand">
      <span class="card__brand-dot"></span>
      <span class="card__brand-name">Pine Ridge Canine Coaching</span>
    </div>
    <h1 class="card__name"><span class="card__name-first">TREVOR</span> HOLLOWAY</h1>
    <p class="card__role">TRAINOR AND OWNER</p>
    <div class="card__divider"></div>
    <div class="contact contact--phone">
      <svg class="contact__icon" viewBox="0 0 30 30"><path d="M8 5l4 5-2 3c1.5 3 4 5.5 7 7l3-2 5 4-3 3C13 24 6 17 5 8z"/><path d="M18 8a5 5 0 0 1 4 4M18 4a9 9 0 0 1 8 8"/></svg>
      <span class="contact__text">+555 304 7162</span>
    </div>
    <div class="contact contact--email">
      <svg class="contact__icon" viewBox="0 0 30 30"><rect x="3" y="7" width="24" height="16"/><path d="M3 7l12 10 12-10M3 23l9-8M27 23l-9-8"/></svg>
      <span class="contact__text">INFO@PINERIDGECANINE.EXAMPLE</span>
    </div>
    <div class="contact contact--web">
      <svg class="contact__icon" viewBox="0 0 30 30"><circle cx="15" cy="15" r="12"/><path d="M3 15h24M15 3c-5 6-5 18 0 24M15 3c5 6 5 18 0 24"/><path d="M19 19l6 3-3 1-1 3z" fill="currentColor"/></svg>
      <span class="contact__text">WWW.PINERIDGECANINE.EXAMPLE</span>
    </div>
    <svg class="card__accent card__accent--bottom" width="120" height="60" viewBox="0 0 120 60"><path d="M0 60 C40 52 80 35 108 0 L120 0 L120 60 Z"/></svg>
  </section>

  <!-- Angled variant -->
  <section class="card card--angled">
    <div class="card__photo" role="img" aria-label="Sepia photo of a trainer standing with three seated dogs on a leafy lawn"></div>
    <svg class="card__accent card__accent--top" width="112" height="38" viewBox="0 0 112 38"><polygon points="0,0 112,0 70,38 0,38"/></svg>
    <div class="card__brand">
      <span class="card__brand-dot"></span>
      <span class="card__brand-name">Pine Ridge Canine Coaching</span>
    </div>
    <h1 class="card__name"><span class="card__name-first">TREVOR</span> HOLLOWAY</h1>
    <p class="card__role">TRAINOR AND OWNER</p>
    <div class="card__divider"></div>
    <div class="contact contact--phone">
      <svg class="contact__icon" viewBox="0 0 30 30"><path d="M8 5l4 5-2 3c1.5 3 4 5.5 7 7l3-2 5 4-3 3C13 24 6 17 5 8z"/><path d="M18 8a5 5 0 0 1 4 4M18 4a9 9 0 0 1 8 8"/></svg>
      <span class="contact__text">+555 304 7162</span>
    </div>
    <div class="contact contact--email">
      <svg class="contact__icon" viewBox="0 0 30 30"><rect x="3" y="7" width="24" height="16"/><path d="M3 7l12 10 12-10M3 23l9-8M27 23l-9-8"/></svg>
      <span class="contact__text">INFO@PINERIDGECANINE.EXAMPLE</span>
    </div>
    <div class="contact contact--web">
      <svg class="contact__icon" viewBox="0 0 30 30"><circle cx="15" cy="15" r="12"/><path d="M3 15h24M15 3c-5 6-5 18 0 24M15 3c5 6 5 18 0 24"/><path d="M19 19l6 3-3 1-1 3z"/></svg>
      <span class="contact__text">WWW.PINERIDGECANINE.EXAMPLE</span>
    </div>
    <svg class="card__accent card__accent--bottom" width="136" height="46" viewBox="0 0 136 46"><polygon points="0,46 54,0 136,0 136,46"/></svg>
  </section>

</body>
</html>
```